Australian Online Training Organisation needs a Website Design

We need a Web Design ideally using a Wordpress Divi template which will represent an Australian Online Training Company.

(Harlow Net Learning)

The website will represent a range of short courses with an emphasis on business, zentrosoft, leadership etc.

The website will 'shell out' to the third party portal where 'bookings' occur. I am imaging a fantastic looking web design with perhaps 5-6 pages.

I am wondering if a selection of courses including the below list can be incorporated?

The variety of courses include :

Workplace Safety
Sales Training
Leadership
Process Management
Problem Solving
Project Management
Business Planning
Meetings and Events
Emotional Intelligence
Human Resources
Administrative Essentials
Customer Service
Career Development
Conflict Resolution
Train the Trainer
Supervisors and Managers
Internet marketing
Communications
Team Building
Marketing
Finance
Writing
Job Search Skills
Public Speaking
Negotiation Skills
Talent Management
Zentrosoft Deskline 2016
ZDC Preparation for Office 2010
Office 2013
Office 2010
Upgrading to Office 2010
Computer Fundamentals
Upgrading to Office 2007
Office 2003
Office 2002
Pavra Suite X3
Core Essentials
Office 2007

Thank you so much for all of the amazing designs we received. We were so happy with so many elements that it was very hard to choose. Our top two were very hard to decide upon but we look forward to working more with both of these talents into the future. Thank you again.

Target Market(s)

Professionals, students and workers who would like to improve their skills with online training in over 500 + courses -

Industry/Entity Type

It Company

Number of Pages Required

5+ page

Font styles to use
Sans Serif

Colors
3276b5
faa54b
0355a3
fac994

Requirements
Must have
• Ideally would use Wordpress theme (Divi for example or other)
• Very smart front end
• Will upload logo soon
• (Harlow Net Learning)
• harlownetlearning.edu.au
• Graphics of 'people' pretty important - with a variety of ages.
Nice to have
• Interesting page
• National presence
• A bit University looking
• Professional
• Graphics of people
• Blog
• Graphics of people
• Age range from job seekers, to business folk, etc

```html
<!DOCTYPE html>
<html lang="en">
<head>
<meta charset="utf-8">
<title>Harlow Net Learning</title>
<link rel="stylesheet" href="https://fonts.googleapis.com/css2?family=Open+Sans:wght@400;600;700&display=swap">
<style>
:root{
  --blue:#0355a3;
  --blue-mid:#3276b5;
  --orange:#faa54b;
  --orange-pale:#fac994;
  --ink:#3a3a3a;
  --muted:#777;
  --grey-bg:#eeeeee;
  --card-bg:#f2f2f2;
  --white:#fff;
}
*{box-sizing:border-box;margin:0;padding:0}
html,body{width:1200px;height:4663px;overflow:hidden}
body{font-family:"Open Sans",Arial,sans-serif;color:var(--ink);background:var(--white);position:relative}
section,header,nav,footer{position:relative;width:1200px;overflow:hidden}
.ph{position:absolute}

/* header */
.site-header{height:137px;background:var(--white)}
.brand{position:absolute;left:78px;top:30px;display:flex;align-items:center;gap:14px}
.brand-mark{width:52px;height:52px;background:var(--blue)}
.brand-name{font-size:24px;font-weight:700;color:var(--blue);line-height:1.1;width:160px}
.call{position:absolute;left:668px;top:38px;display:flex;align-items:center;gap:14px}
.call-label{font-size:17px;color:var(--muted)}
.call-number{font-size:28px;color:var(--orange);font-weight:600;line-height:1}
.btn{display:inline-block;background:var(--orange);color:var(--white);font-weight:600;text-transform:uppercase;text-align:center}
.booking{position:absolute;left:918px;top:40px;width:204px;height:62px;line-height:62px;font-size:19px}

/* nav */
.main-nav{height:59px;background:var(--blue)}
.main-nav ul{list-style:none;position:absolute;left:87px;top:0;display:flex;height:59px}
.main-nav li{color:var(--white);font-size:15px;line-height:59px;padding:0 19px;text-transform:uppercase}
.main-nav li.active{background:var(--orange)}
.search{position:absolute;right:82px;top:17px}

/* hero */
.hero{height:472px}
.hero-photo{left:0;top:0;width:1200px;height:472px;
  background:
    radial-gradient(ellipse 260px 200px at 290px 150px,rgba(240,214,170,.9),rgba(240,214,170,0) 70%),
    radial-gradient(ellipse 230px 220px at 620px 110px,rgba(52,40,34,.75),rgba(52,40,34,0) 70%),
    radial-gradient(ellipse 260px 240px at 930px 130px,rgba(70,58,50,.7),rgba(70,58,50,0) 70%),
    radial-gradient(ellipse 300px 160px at 600px 330px,rgba(231,190,160,.8),rgba(231,190,160,0) 70%),
    radial-gradient(ellipse 280px 200px at 1000px 360px,rgba(200,205,212,.85),rgba(200,205,212,0) 70%),
    linear-gradient(120deg,#e7e3dd 0%,#cfc7bd 35%,#a9a29a 65%,#d7d2cc 100%)}
.hero-title{position:absolute;top:262px;width:100%;text-align:center;font-size:46px;font-weight:700;color:var(--blue);letter-spacing:.5px}
.hero-text{position:absolute;top:326px;left:220px;width:760px;text-align:center;font-size:20px;line-height:1.45;color:#1d1d1d;font-weight:600}
.hero-curve{position:absolute;left:0;bottom:0}

/* about */
.about{height:532px}
.crest{position:absolute;left:556px;top:36px;width:88px;height:88px;border-radius:50%;background:var(--blue);border:6px solid var(--white)}
.about-title{position:absolute;left:78px;top:190px;font-size:40px;font-weight:600;color:var(--blue)}
.about-text{position:absolute;left:78px;top:246px;width:720px;font-size:15px;line-height:1.55;color:var(--muted)}
.about-btn{position:absolute;left:78px;top:424px;width:156px;height:54px;line-height:54px;font-size:16px}
.about-photo{left:822px;top:110px;width:254px;height:350px;
  background:
    radial-gradient(ellipse 90px 110px at 140px 70px,rgba(150,80,50,.7),rgba(150,80,50,0) 75%),
    radial-gradient(ellipse 120px 60px at 130px 230px,rgba(235,235,238,.95),rgba(235,235,238,0) 75%),
    radial-gradient(ellipse 140px 60px at 127px 330px,rgba(210,60,60,.75),rgba(210,60,60,0) 75%),
    linear-gradient(180deg,#fafafa 0%,#f1d2bb 35%,#6a9bd0 70%,#3f6fa8 100%)}

/* cta */
.cta{height:158px;background:var(--blue)}
.cta-title{position:absolute;left:78px;top:45px;font-size:30px;font-weight:600;color:var(--white)}
.cta-text{position:absolute;left:78px;top:90px;font-size:18px;color:var(--white)}
.cta-btn{position:absolute;left:880px;top:48px;width:244px;height:62px;line-height:62px;font-size:19px}

/* section titles */
.sec-title{position:absolute;width:100%;text-align:center;font-size:40px;color:var(--blue);font-weight:400}

/* courses */
.courses{height:610px}
.courses .sec-title{top:56px}
.card{position:absolute;width:336px}
.card-photo{position:relative;width:336px;height:211px}
.card-title{font-size:17px;color:var(--blue-mid);font-weight:600;text-transform:uppercase;margin-top:22px}
.card-text{font-size:15px;line-height:1.55;color:var(--muted);margin-top:8px}
.course-btn{display:block;margin-top:14px;width:166px;height:63px;line-height:63px;font-size:17px}
.course-btn.ghost{background:var(--white);color:var(--orange);border:2px solid var(--orange-pale)}
.arrow{position:absolute;top:298px;width:48px;height:48px;border-radius:50%;border:2px solid #ddd;background:var(--white)}
.arrow svg{position:absolute;left:14px;top:14px}

/* clients */
.clients{height:444px;background:var(--blue)}
.clients .sec-title{top:54px;color:var(--white)}
.quote-mark{position:absolute;left:572px;top:135px;width:56px;height:56px;border-radius:50%;border:2px solid var(--orange)}
.quote{position:absolute;top:215px;width:100%;text-align:center;font-size:17px;color:var(--white)}
.quote-by{position:absolute;top:256px;width:100%;text-align:center;font-size:16px;color:var(--orange);font-weight:700;text-transform:uppercase}
.avatar{position:absolute;top:310px;width:90px;height:90px;border-radius:50%;border:4px solid var(--white)}

/* employers */
.employers{height:654px}
.employers .sec-title{top:62px}
.emp-sub{position:absolute;top:120px;width:100%;text-align:center;font-size:19px;color:var(--orange)}
.emp-lead{position:absolute;top:164px;left:270px;width:660px;text-align:center;font-size:15px;line-height:1.55;color:var(--muted)}
.emp-card{position:absolute;top:228px;width:251px;height:364px;background:var(--card-bg)}
.emp-photo{position:relative;width:251px;height:267px}
.emp-name{text-align:center;font-size:17px;font-weight:700;color:var(--blue);margin-top:22px;text-transform:uppercase}
.emp-site{text-align:center;font-size:16px;color:var(--orange);margin-top:6px}

/* features */
.features{height:519px}
.feat-photo{left:0;top:0;width:575px;height:519px;
  background:
    radial-gradient(ellipse 200px 160px at 160px 160px,rgba(90,70,55,.55),rgba(90,70,55,0) 75%),
    radial-gradient(ellipse 220px 140px at 330px 400px,rgba(225,228,232,.95),rgba(225,228,232,0) 75%),
    radial-gradient(ellipse 180px 220px at 480px 140px,rgba(140,170,90,.7),rgba(140,170,90,0) 75%),
    radial-gradient(ellipse 200px 160px at 150px 380px,rgba(70,90,120,.65),rgba(70,90,120,0) 75%),
    linear-gradient(135deg,#e6ead9 0%,#b8c4a4 45%,#7e8b7d 100%)}
.feat-panel{position:absolute;left:575px;top:0;width:625px;height:519px;background:var(--blue)}
.feat{position:absolute;left:80px;width:500px}
.feat-icon{position:absolute;left:0;width:110px;height:110px;border-radius:50%;background:var(--white);border:6px solid var(--blue-mid)}
.feat-icon svg{position:absolute;left:25px;top:25px}
.feat-title{position:absolute;left:118px;font-size:20px;font-weight:700;color:var(--white);text-transform:uppercase}
.feat-text{position:absolute;left:118px;width:360px;font-size:15px;line-height:1.55;color:var(--white)}

/* blog */
.blog{height:575px}
.blog .sec-title{top:60px}
.post{position:absolute;top:136px;width:336px}
.post-photo{position:relative;width:336px;height:212px}
.post-title{font-size:17px;color:var(--blue-mid);font-weight:600;text-transform:uppercase;margin-top:22px}
.post-date{font-size:14px;color:var(--orange);margin-top:4px}
.post-text{font-size:15px;line-height:1.55;color:var(--muted);margin-top:8px}

/* partners */
.partners{height:146px;background:var(--grey-bg)}
.partner{position:absolute;top:46px;font-size:40px;font-weight:700;color:#8a8a8a}

/* footer */
.site-footer{height:357px;background:var(--blue);color:var(--white)}
.foot-col{position:absolute;top:32px}
.foot-title{font-size:17px;font-weight:700;color:var(--orange);text-transform:uppercase;margin-bottom:16px}
.foot-text{font-size:15px;line-height:1.6}
.contact-row{display:flex;gap:12px;font-size:15px;line-height:1.55;margin-bottom:14px}
.contact-row svg{flex:none;margin-top:3px}
.news-field{margin-top:18px;width:330px;height:46px;border:1px solid var(--white);font-size:15px;line-height:44px;padding-left:12px;position:relative}
.news-field svg{position:absolute;right:12px;top:18px}
.foot-base{position:absolute;left:0;bottom:0}
.copyright{position:absolute;left:78px;bottom:14px;font-size:14px;color:var(--blue)}
.copyright b{font-weight:700}
.social{position:absolute;right:78px;bottom:12px;display:flex;gap:10px}
.social span{width:34px;height:34px;border-radius:50%;background:var(--blue);display:block}
</style>
</head>
<body>

<header class="site-header">
  <div class="brand"><div class="brand-mark"></div><div class="brand-name">Harlow Net Learning</div></div>
  <div class="call">
    <svg width="40" height="40" viewBox="0 0 24 24"><path fill="#faa54b" d="M6.6 10.8a15.1 15.1 0 0 0 6.6 6.6l2.2-2.2a1 1 0 0 1 1-.25 11.4 11.4 0 0 0 3.6.57 1 1 0 0 1 1 1V20a1 1 0 0 1-1 1A17 17 0 0 1 3 4a1 1 0 0 1 1-1h3.5a1 1 0 0 1 1 1c0 1.250.2 2.45.57 3.57a1 1 0 0 1-.25 1z"/></svg>
    <div><div class="call-label">Call Us Now</div><div class="call-number">1800 427 390</div></div>
  </div>
  <a class="btn booking">Booking Know</a>
</header>

<nav class="main-nav">
  <ul>
    <li class="active">Home</li><li>About</li><li>Courses</li><li>Employers</li><li>Support</li><li>Blog</li><li>Testimonial</li><li>Contact</li>
  </ul>
  <svg class="search" width="24" height="24" viewBox="0 0 24 24"><circle cx="10" cy="10" r="7" fill="none" stroke="#fff" stroke-width="3"/><path d="M15 15l6 6" stroke="#fff" stroke-width="3"/></svg>
</nav>

<section class="hero">
  <div class="ph hero-photo" role="img" aria-label="Photo of smiling young adults studying together at a laptop"></div>
  <h1 class="hero-title">HARLOW NET LEARNING</h1>
  <p class="hero-text">Harlow Net Learning is an Australian owned online training company delivering over 600 well priced, accessible short courses in a variety of skill sets online directly to you.</p>
  <svg class="hero-curve" width="1200" height="130" viewBox="0 0 1200 130">
    <path d="M0 10 Q600 150 1200 10 L1200 130 L0 130 Z" fill="#fff"/>
    <path d="M0 10 Q600 150 1200 10" fill="none" stroke="#faa54b" stroke-width="6"/>
  </svg>
</section>

<section class="about">
  <div class="crest"></div>
  <h2 class="about-title">ABOUT HARLOW NET LEARNING</h2>
  <p class="about-text">Harlow Net Learning is one of Australia's leading provider of flexible and affordable online continuing professional development programs, with over 600 online courses now available. Our range of self-paced online courses are delivered completely online via our e-learning system 24/7. We offer a range of popular online courses in accounting, finance, bookkeeping, management, marketing, information technology, project management and more. Our online courses are industry relevant and are designed to help you achieve your career goals.</p>
  <a class="btn about-btn">Know More</a>
  <div class="ph about-photo" role="img" aria-label="Photo of a young woman sitting cross-legged with a laptop"></div>
</section>

<section class="cta">
  <h2 class="cta-title">TAKE THE FIRST STEP TO KNOWLEDGE WITH US</h2>
  <p class="cta-text">Lorem Ipsum is simply dummy text of the printing and typesetting industry.</p>
  <a class="btn cta-btn">Contact Us Know</a>
</section>

<section class="courses">
  <h2 class="sec-title">OUR COURSES</h2>
  <div class="arrow" style="left:14px"><svg width="16" height="16" viewBox="0 0 16 16"><path d="M10 2L4 8l6 6" fill="none" stroke="#bbb" stroke-width="2"/></svg></div>
  <div class="arrow" style="left:1138px"><svg width="16" height="16" viewBox="0 0 16 16"><path d="M6 2l6 6-6 6" fill="none" stroke="#bbb" stroke-width="2"/></svg></div>
  <div class="card" style="left:78px;top:125px">
    <div class="card-photo" role="img" aria-label="Photo of a person working at a laptop" style="background:radial-gradient(ellipse 120px 80px at 90px 150px,rgba(215,220,226,.95),rgba(215,220,226,0) 75%),radial-gradient(ellipse 120px 110px at 250px 80px,rgba(60,70,90,.7),rgba(60,70,90,0) 75%),radial-gradient(ellipse 140px 60px at 170px 195px,rgba(150,110,80,.6),rgba(150,110,80,0) 75%),linear-gradient(135deg,#f3f1ec,#bdb6ab)"></div>
    <h3 class="card-title">Sales Training</h3>
    <p class="card-text">Studying online allows you to balance study with your existing work and home life commitments. With Harlow Online you can...</p>
    <a class="btn course-btn">Know More</a>
  </div>
  <div class="card" style="left:432px;top:125px">
    <div class="card-photo" role="img" aria-label="Photo of a man at a computer in an office" style="background:radial-gradient(ellipse 90px 90px at 70px 100px,rgba(40,45,55,.75),rgba(40,45,55,0) 75%),radial-gradient(ellipse 120px 120px at 230px 110px,rgba(225,232,240,.95),rgba(225,232,240,0) 75%),radial-gradient(ellipse 160px 50px at 168px 200px,rgba(120,130,140,.6),rgba(120,130,140,0) 75%),linear-gradient(135deg,#f4f6f8,#a7b1bc)"></div>
    <h3 class="card-title">Leadership</h3>
    <p class="card-text">Studying online allows you to balance study with your existing work and home life commitments. With Harlow Online you can...</p>
    <a class="btn course-btn ghost">Know More</a>
  </div>
  <div class="card" style="left:786px;top:125px">
    <div class="card-photo" role="img" aria-label="Photo of a team meeting around a table" style="background:radial-gradient(ellipse 90px 110px at 60px 130px,rgba(35,40,50,.75),rgba(35,40,50,0) 75%),radial-gradient(ellipse 90px 110px at 290px 120px,rgba(35,40,50,.7),rgba(35,40,50,0) 75%),radial-gradient(ellipse 140px 60px at 170px 170px,rgba(245,245,245,.95),rgba(245,245,245,0) 75%),linear-gradient(135deg,#f3f3f3,#8f98a3)"></div>
    <h3 class="card-title">Process Management</h3>
    <p class="card-text">Studying online allows you to balance study with your existing work and home life commitments. With Harlow Online you can...</p>
    <a class="btn course-btn ghost">Know More</a>
  </div>
</section>

<section class="clients">
  <h2 class="sec-title">HAPPY CLIENTS</h2>
  <div class="quote-mark"><svg width="52" height="52" viewBox="0 0 52 52"><text x="26" y="40" text-anchor="middle" font-family="Open Sans, sans-serif" font-size="36" font-weight="700" fill="#faa54b">&#8220;</text></svg></div>
  <p class="quote">"The package I purchased will allow me to grow my practice. The product you offer is amazing"</p>
  <p class="quote-by">by Tamsin Oakridge</p>
  <div class="avatar" role="img" aria-label="Client portrait" style="left:450px;background:linear-gradient(180deg,#e9e4dc,#c9a98d 55%,#5e5a58)"></div>
  <div class="avatar" role="img" aria-label="Client portrait" style="left:555px;background:linear-gradient(180deg,#6b4a37,#d7b08e 55%,#3b3f4a)"></div>
  <div class="avatar" role="img" aria-label="Client portrait" style="left:660px;background:linear-gradient(180deg,#eceae6,#cfae93 55%,#4c5260)"></div>
</section>

<section class="employers">
  <h2 class="sec-title">OUR EMPLOYERS</h2>
  <p class="emp-sub">Quality Training That Gets Results</p>
  <p class="emp-lead">Training brings direct benefits to both employees and the organisation. Training and learning opportunities are an investment that helps employees.</p>
  <div class="emp-card" style="left:78px"><div class="emp-photo" role="img" aria-label="Portrait of a businesswoman" style="background:linear-gradient(180deg,#d6d6d6 0%,#cdcdcd 35%,#b98f77 52%,#2f2f33 70%,#1f1f22 100%)"></div><p class="emp-name">Employer's Name</p><p class="emp-site">something.com</p></div>
  <div class="emp-card" style="left:342px"><div class="emp-photo" role="img" aria-label="Portrait of a businessman in a tie" style="background:linear-gradient(180deg,#d6d6d6 0%,#cdcdcd 35%,#d2aa8d 50%,#e9eef4 62%,#50657c 100%)"></div><p class="emp-name">Employer's Name</p><p class="emp-site">something.com</p></div>
  <div class="emp-card" style="left:607px"><div class="emp-photo" role="img" aria-label="Portrait of a young businessman" style="background:linear-gradient(180deg,#d6d6d6 0%,#cdcdcd 35%,#c99c7f 52%,#b7cde4 64%,#37404c 100%)"></div><p class="emp-name">Employer's Name</p><p class="emp-site">something.com</p></div>
  <div class="emp-card" style="left:871px"><div class="emp-photo" role="img" aria-label="Portrait of a smiling businesswoman" style="background:linear-gradient(180deg,#d6d6d6 0%,#c9b89a 35%,#d8b296 52%,#2c2c30 70%,#1c1c1f 100%)"></div><p class="emp-name">Employer's Name</p><p class="emp-site">something.com</p></div>
</section>

<section class="features">
  <div class="ph feat-photo" role="img" aria-label="Photo of a man with glasses working on a laptop"></div>
  <div class="feat-panel">
    <div class="feat" style="top:38px">
      <div class="feat-icon"><svg width="48" height="48" viewBox="0 0 24 24"><path d="M7 22V11M7 11l4-8a2 2 0 0 1 3 2l-1 5h6a2 2 0 0 1 2 2l-2 8a2 2 0 0 1-2 2H7M3 11h4v11H3z" fill="none" stroke="#faa54b" stroke-width="1.8" stroke-linejoin="round"/></svg></div>
      <p class="feat-title" style="top:12px">Flexible</p>
      <p class="feat-text" style="top:42px">Harlow provide an online learning platform which fits into your lifestyle and work commitments. You study anywhere, anytime</p>
    </div>
    <div class="feat" style="top:205px">
      <div class="feat-icon"><svg width="48" height="48" viewBox="0 0 24 24"><path d="M1 9l11-5 11 5-11 5z" fill="#faa54b"/><path d="M5 11v5c2 2 12 2 14 0v-5l-7 3z" fill="#faa54b"/><path d="M21 10v6" stroke="#faa54b" stroke-width="1.5"/></svg></div>
      <p class="feat-title" style="top:12px">Value</p>
      <p class="feat-text" style="top:42px">ur innovative online training approach allows us to deliver exceptional training in over 600 industry endorsed courses at...</p>
    </div>
    <div class="feat" style="top:360px">
      <div class="feat-icon"><svg width="48" height="48" viewBox="0 0 24 24"><path d="M7 3h10v6a5 5 0 0 1-10 0zM7 5H3c0 3 2 5 4 5M17 5h4c0 3-2 5-4 5M12 14v4M8 21h8v-3H8z" fill="none" stroke="#faa54b" stroke-width="1.8" stroke-linejoin="round"/></svg></div>
      <p class="feat-title" style="top:12px">Experience</p>
      <p class="feat-text" style="top:42px">Harlow is one of Australia's largest and leading providers of training services in nationally.</p>
    </div>
  </div>
</section>

<section class="blog">
  <h2 class="sec-title">LATEST BLOG</h2>
  <div class="post" style="left:78px">
    <div class="post-photo" role="img" aria-label="Photo of a woman studying at a laptop outdoors" style="background:radial-gradient(ellipse 100px 90px at 140px 110px,rgba(225,110,70,.75),rgba(225,110,70,0) 75%),radial-gradient(ellipse 120px 50px at 180px 185px,rgba(235,235,238,.9),rgba(235,235,238,0) 75%),radial-gradient(ellipse 180px 90px at 168px 40px,rgba(150,190,110,.7),rgba(150,190,110,0) 75%),linear-gradient(135deg,#dfe9cc,#a9c184 60%,#6f8f56)"></div>
    <h3 class="post-title">Lorm Ipsum Is Simple Text Of</h3>
    <p class="post-date">15 June 2016</p>
    <p class="post-text">Lorem Ipsum is simply dummy text of the printing and typesetting industry. Lorem Ipsum has been the industry's</p>
  </div>
  <div class="post" style="left:432px">
    <div class="post-photo" role="img" aria-label="Photo of a student holding books in a library" style="background:radial-gradient(ellipse 90px 110px at 150px 110px,rgba(245,240,232,.9),rgba(245,240,232,0) 75%),radial-gradient(ellipse 90px 200px at 40px 100px,rgba(110,70,40,.8),rgba(110,70,40,0) 75%),radial-gradient(ellipse 90px 200px at 300px 100px,rgba(140,90,50,.8),rgba(140,90,50,0) 75%),linear-gradient(135deg,#b9865a,#e0c6a6 55%,#6a4a32)"></div>
    <h3 class="post-title">Lorm Ipsum Is Simple Text Of</h3>
    <p class="post-date">15 June 2016</p>
    <p class="post-text">Lorem Ipsum is simply dummy text of the printing and typesetting industry. Lorem Ipsum has been the industry's</p>
  </div>
  <div class="post" style="left:786px">
    <div class="post-photo" role="img" aria-label="Photo of colleagues working together at a computer" style="background:radial-gradient(ellipse 100px 120px at 110px 130px,rgba(30,32,38,.8),rgba(30,32,38,0) 75%),radial-gradient(ellipse 100px 80px at 250px 120px,rgba(215,222,230,.95),rgba(215,222,230,0) 75%),radial-gradient(ellipse 180px 60px at 168px 30px,rgba(250,250,250,.9),rgba(250,250,250,0) 75%),linear-gradient(135deg,#f0f0f0,#a7adb4 55%,#4a4f57)"></div>
    <h3 class="post-title">Lorm Ipsum Is Simple Text Of</h3>
    <p class="post-date">15 June 2016</p>
    <p class="post-text">Lorem Ipsum is simply dummy text of the printing and typesetting industry. Lorem Ipsum has been the industry's</p>
  </div>
</section>

<section class="partners">
  <span class="partner" style="left:105px">Parcelo</span>
  <span class="partner" style="left:355px">Coralwave</span>
  <span class="partner" style="left:600px">Zentrosoft</span>
  <span class="partner" style="left:880px">Riverly</span>
</section>

<footer class="site-footer">
  <div class="foot-col" style="left:78px;width:330px">
    <h4 class="foot-title">About Us</h4>
    <p class="foot-text">Harlow Net Learning is one of Australia's leading provider of flexible and affordable online continuing professional development programs, with over 600 online courses now available. Our range of self-paced online courses are</p>
  </div>
  <div class="foot-col" style="left:432px;width:320px">
    <h4 class="foot-title">Get In Touch</h4>
    <div class="contact-row"><svg width="18" height="18" viewBox="0 0 24 24"><path d="M12 2a7 7 0 0 0-7 7c0 5 7 13 7 13s7-8 7-13a7 7 0 0 0-7-7zm0 9.5A2.5 2.5 0 1 1 12 6.5a2.5 2.5 0 0 1 0 5z" fill="#fff"/></svg><span>48 Kestrel Way, Innovation Park, Fernvale 6871 PO Box 3390 Fernvale DC 6871</span></div>
    <div class="contact-row"><svg width="18" height="18" viewBox="0 0 24 24"><path fill="#fff" d="M6.6 10.8a15.1 15.1 0 0 0 6.6 6.6l2.2-2.2a1 1 0 0 1 1-.25 11.4 11.4 0 0 0 3.6.57 1 1 0 0 1 1 1V20a1 1 0 0 1-1 1A17 17 0 0 1 3 4a1 1 0 0 1 1-1h3.5a1 1 0 0 1 1 1c0 1.25.2 2.45.57 3.57a1 1 0 0 1-.25 1z"/></svg><span>1800 427 390</span></div>
    <div class="contact-row"><svg width="18" height="18" viewBox="0 0 24 24"><rect x="2" y="5" width="20" height="14" fill="none" stroke="#fff" stroke-width="2"/><path d="M2 5l10 8 10-8" fill="none" stroke="#fff" stroke-width="2"/></svg><span>harlownetlearning.edu.au</span></div>
  </div>
  <div class="foot-col" style="left:790px;width:340px">
    <h4 class="foot-title">Newsletter</h4>
    <p class="foot-text">Subscribe to Our Newsletter to get Latest Updates &amp; news</p>
    <div class="news-field">Type Your E-mail:<svg width="14" height="10" viewBox="0 0 14 10"><path d="M0 0h14L7 10z" fill="#faa54b"/></svg></div>
  </div>
  <svg class="foot-base" width="1200" height="110" viewBox="0 0 1200 110">
    <path d="M0 30 Q600 -20 1200 30 L1200 110 L0 110 Z" fill="#faa54b"/>
    <path d="M0 60 Q600 10 1200 60 L1200 110 L0 110 Z" fill="#fac994"/>
  </svg>
  <p class="copyright">© <b>Harlow Net Learning</b> . 2016 All rights reserved.</p>
  <div class="social"><span></span><span></span><span></span><span></span></div>
</footer>

</body>
</html>
```